card design for engineering consultancy

engineering drafting and project management company the provides drafting services for.
Electrical, Hydraulic, Mechanical, and Civil services
The company is called Q7R Services and logo is as attached
Information on card should be.
1. Logo
2.website : Q7RServices.example
3. email : info@Q7RServices.example
4. Phone: (+61) 400512836
5. Motto: Design - Document - Develop - Deliver

this card should be basically used for business identification only

Target Market(s)

electricians plumbers air conditioning installers and civil contractors

Industry/Entity Type

engineering, drafting, electrical, plumbing, airconditioning, civil

Contact Information for Business Card

1. Logo 2.website : Q7RServices.example 3. email : info@Q7RServices.example 4. Phone: (+61) 400512836 5. Motto: Design - Document - Develop - Deliver

Font styles to use
Serif

Requirements
Must have
• logo
Nice to have
• something inovative and different that makes it stand out from being just another business card

```html
<!DOCTYPE html>
<html lang="en">
<head>
<meta charset="utf-8">
<title>Q7R Services – Business Card</title>
<link rel="stylesheet" href="https://fonts.googleapis.com/css2?family=Michroma&display=swap">
<style>
  :root {
    --page-bg: #d9d9d9;
    --card-black: #0d0d0e;
    --card-charcoal: #1c1c1e;
    --brand-red: #e30e16;
    --deep-red: #9e0c10;
    --logo-grey: #5b5755;
    --silver: #c9c9cb;
    --ink: #0a0a0a;
  }
  * { box-sizing: border-box; margin: 0; padding: 0; }
  html, body {
    width: 1200px; height: 846px; overflow: hidden;
    background: var(--page-bg);
    font-family: "Michroma", sans-serif;
  }
  .sheet {
    width: 1200px; height: 846px;
    display: flex; align-items: center; justify-content: center; gap: 30px;
  }
  .card {
    position: relative; width: 560px; height: 330px; overflow: hidden;
    background: var(--card-black);
    box-shadow: 0 10px 24px rgba(0,0,0,.25);
  }

  /* front */
  .tech-panel {
    position: absolute; left: 0; top: 0; width: 250px; height: 150px;
    background: linear-gradient(135deg, #1a1a1c 0%, #262628 55%, #4a0d10 100%);
  }
  .red-band {
    position: absolute; left: 0; right: 0; top: 158px; height: 100px;
    background: var(--brand-red);
    clip-path: polygon(110px 0, 100% 0, 100% 100%, 60px 100%);
  }
  .base-band {
    position: absolute; left: 0; bottom: 10px; width: 150px; height: 12px;
    background: var(--deep-red);
    clip-path: polygon(0 0, 100% 0, 92% 100%, 0 100%);
  }
  .front-name {
    position: absolute; top: 56px; right: 34px;
    display: flex; align-items: center; gap: 12px;
    color: var(--logo-grey); font-size: 22px; letter-spacing: 2px; text-transform: uppercase;
    white-space: nowrap;
  }
  .front-name .mark { width: 18px; height: 18px; background: var(--brand-red); }
  .contact-list {
    position: absolute; left: 180px; top: 172px; list-style: none;
    color: var(--ink); font-size: 13px; text-transform: uppercase; letter-spacing: .3px;
  }
  .contact-list li { display: flex; align-items: center; gap: 8px; height: 24px; white-space: nowrap; }
  .contact-list svg { width: 16px; height: 16px; flex: none; }
  .motto {
    position: absolute; left: 160px; top: 278px;
    color: var(--brand-red); font-size: 11.5px; letter-spacing: .8px; text-transform: uppercase;
    white-space: nowrap;
  }

  /* back */
  .card-back { background: radial-gradient(circle at 40% 60%, var(--card-charcoal), var(--card-black) 70%); }
  .back-name {
    position: absolute; inset: 0; display: flex; align-items: center; justify-content: center;
    color: var(--silver); font-size: 30px; letter-spacing: 3px; text-transform: uppercase;
  }
</style>
</head>
<body>
<main class="sheet">

  <section class="card card-front" aria-label="Card front">
    <div class="tech-panel" role="img" aria-label="Decorative dark tech-line pattern with red accents"></div>
    <div class="red-band"></div>
    <div class="base-band"></div>

    <div class="front-name"><span class="mark"></span>Q7R Services</div>

    <ul class="contact-list">
      <li>
        <svg viewBox="0 0 16 16" aria-hidden="true"><circle cx="8" cy="8" r="7.5" fill="var(--ink)"/><g fill="none" stroke="var(--brand-red)" stroke-width="1"><circle cx="8" cy="8" r="5"/><ellipse cx="8" cy="8" rx="2" ry="5"/><line x1="3" y1="8" x2="13" y2="8"/></g></svg>
        www.Q7RServices.example
      </li>
      <li>
        <svg viewBox="0 0 16 16" aria-hidden="true"><circle cx="8" cy="8" r="7.5" fill="var(--ink)"/><g fill="none" stroke="var(--brand-red)" stroke-width="1"><rect x="3.5" y="5" width="9" height="6"/><polyline points="3.5,5 8,9 12.5,5"/></g></svg>
        info@Q7RServices.example
      </li>
      <li>
        <svg viewBox="0 0 16 16" aria-hidden="true"><circle cx="8" cy="8" r="7.5" fill="var(--ink)"/><path d="M5 4.5 L6.6 4.5 L7.2 6.6 L6.2 7.4 Q7 9 8.6 9.8 L9.4 8.8 L11.5 9.4 L11.5 11 Q7.5 11.5 5 7.5 Z" fill="var(--brand-red)"/></svg>
        (+61) 400512836
      </li>
    </ul>

    <p class="motto">Design - Document - Develop - Deliver</p>
  </section>

  <section class="card card-back" aria-label="Card back">
    <div class="back-name">Q7R Services</div>
  </section>

</main>
</body>
</html>
```